Design interface for an invoicing software

We are developing a new invoicing software that is a very boring topic. Users can use the software to write invoices and manage their income. Therefore we want to inspire the users with a great desgin. By this we mean, for example, the use of photos in the background (streets in New York, landscapes), or "crazy" looking headlines or something else. Target group are young start-ups, freelancers, hairdressers and taxi drivers at the age of 18-40 years. It would also be worth considering to adapt the look to the user's industry. However, the menu items themselves and the approximate position of the information are given. See file "startpoint" What kind of ideas do you have?

Europe

Small Business

Designer to choose colors to be used in the design.

• the menu items themselves and the approximate position of the information are given. The navigation menu itself can be different.
• boring look and feel

```html
<!DOCTYPE html>
<html lang="en">
<head>
<meta charset="utf-8">
<title>Ledgerly – Invoicing Dashboard</title>
<link href="https://fonts.googleapis.com/css2?family=Roboto:wght@300;400;500;700&display=swap" rel="stylesheet">
<style>
:root{
  --page:#fbfbfe;
  --panel:#ffffff;
  --main:#f4f5fd;
  --indigo:#2d2a8c;
  --indigo-soft:#b3b1dc;
  --orange:#f58a4b;
  --amber:#ffb300;
  --ink:#333340;
  --muted:#8a8a96;
  --line:#d9d9e3;
  --danger:#f2294e;
}
*{box-sizing:border-box;margin:0;padding:0}
html,body{width:1200px;height:1200px;overflow:hidden}
body{background:var(--page);font-family:'Roboto',sans-serif;color:var(--ink);position:relative}
.decor{position:absolute;left:0;top:0}
.app{position:absolute;left:54px;top:124px;width:1092px;height:953px;background:var(--main);box-shadow:0 20px 60px rgba(45,42,140,.12);overflow:hidden}
.topbar{position:absolute;left:0;top:0;width:100%;height:80px;background:var(--panel);box-shadow:0 2px 8px rgba(0,0,0,.04);z-index:2}
.brand{position:absolute;left:10px;top:20px;display:flex;flex-direction:column;align-items:center;gap:6px}
.brand-mark{width:30px;height:30px;background:var(--indigo);border-radius:4px}
.brand-name{font-size:12px;font-weight:500;color:#555;letter-spacing:.3px}
.avatar{position:absolute;left:951px;top:18px;width:43px;height:43px;border-radius:50%;background:radial-gradient(circle at 50% 45%,#c99a80,#4a3328)}
.user{position:absolute;left:1008px;top:33px;font-size:14px;font-weight:500;color:#666;display:flex;gap:14px;align-items:center}
.user .caret{font-size:9px}
.sidebar{position:absolute;left:0;top:80px;width:80px;height:873px;background:var(--panel)}
.nav-item{position:absolute;left:0;width:80px;text-align:center;font-size:9.5px;line-height:12px;letter-spacing:.3px;color:var(--muted);text-transform:uppercase}
.nav-item svg{display:block;margin:0 auto 4px}
.nav-item.active{color:var(--indigo);font-weight:500}
.notice{position:absolute;left:100px;top:128px;font-size:11.5px;color:#777;display:flex;align-items:center;gap:5px}
.search{position:absolute;left:629px;top:116px;width:357px;height:25px;border-bottom:1px solid #c8c8d4;font-size:11px;color:#aaa;padding:3px 11px}
.search svg{position:absolute;right:8px;top:2px}
.fab{position:absolute;left:1018px;top:98px;width:56px;height:56px;border-radius:50%;background:radial-gradient(circle at 45% 40%,#ffc21a,#ff9f00);box-shadow:0 10px 20px rgba(255,160,0,.4)}
.fab::before,.fab::after{content:"";position:absolute;background:#fff;border-radius:2px;left:50%;top:50%;transform:translate(-50%,-50%)}
.fab::before{width:30px;height:5px}.fab::after{width:5px;height:30px}
.title{position:absolute;left:120px;font-size:24px;font-weight:400;letter-spacing:1px;color:#444}
.card{position:absolute;background:var(--panel);border-radius:6px}
.pill{position:absolute;height:19px;border:1px solid #777;border-radius:10px;font-size:10.5px;color:#444;display:flex;align-items:center;justify-content:center}
.pill.on{background:var(--indigo);border-color:var(--indigo);color:#fff;font-weight:500}
.chart{position:absolute;left:0;top:0}
.totals h3{position:absolute;left:22px;top:11px;font-size:12px;font-weight:500;color:#333}
.totals .label{position:absolute;left:22px;font-size:9.5px;color:var(--muted)}
.totals .value{position:absolute;left:22px;font-size:20px;letter-spacing:1px;color:#333}
.row{position:absolute;left:0;width:940px;height:20px;font-size:11.5px;letter-spacing:.4px;color:#333}
.row span{position:absolute;top:3px}
.check{position:absolute;left:18px;top:4px;width:12px;height:12px;border:2px solid #444;border-radius:1px}
.check.done{background:#444}
.row svg{position:absolute;top:2px}
.scroll{position:absolute;left:951px;top:11px;width:7px;height:252px;border-radius:4px;background:#eceaf6}
.scroll i{position:absolute;left:0;top:8px;width:7px;height:59px;border-radius:4px;background:var(--indigo)}
</style>
</head>
<body>
<svg class="decor" width="1200" height="1200" aria-hidden="true">
  <polygon points="456,26 632,124 560,124" fill="var(--indigo-soft)"/>
  <polygon points="1146,406 1200,436 1200,832 1146,858" fill="var(--indigo-soft)"/>
  <polygon points="620,1077 698,1077 448,1200" fill="var(--indigo-soft)"/>
</svg>

<div class="app">
  <header class="topbar">
    <div class="brand"><div class="brand-mark"></div><div class="brand-name">Ledgerly</div></div>
    <div class="avatar" role="img" aria-label="User profile photo"></div>
    <div class="user">Micheal <span class="caret">▼</span></div>
  </header>

  <nav class="sidebar">
    <div class="nav-item active" style="top:33px"><svg width="18" height="18" viewBox="0 0 24 24" fill="none" stroke="var(--indigo)" stroke-width="2.4"><path d="M12 4a9 9 0 1 1-8 5"/><path d="M12 13l-3-4"/><path d="M10 2h4"/></svg>Dashboard</div>
    <div class="nav-item" style="top:76px"><svg width="17" height="17" viewBox="0 0 24 24" fill="none" stroke="#999" stroke-width="2"><rect x="3" y="5" width="18" height="16" rx="2"/><path d="M3 9h18M8 3v4M16 3v4M9 15l2 2 4-4"/></svg>Calender</div>
    <div class="nav-item" style="top:121px"><svg width="18" height="16" viewBox="0 0 24 20" fill="#999"><circle cx="8" cy="6" r="3.5"/><circle cx="16" cy="6" r="3.5"/><path d="M1 18c0-4 3-6 7-6s7 2 7 6zM14 12c4 0 9 1 9 6h-7c0-3-1-5-2-6z"/></svg>Customers</div>
    <div class="nav-item" style="top:178px"><svg width="17" height="15" viewBox="0 0 24 20" fill="#999"><path d="M2 3h20v14H2z"/><path d="M2 3l10 7 10-7" stroke="#fff" stroke-width="2" fill="none"/></svg>Messages</div>
    <div class="nav-item" style="top:221px"><svg width="17" height="15" viewBox="0 0 24 20" fill="none" stroke="#999" stroke-width="2"><rect x="2" y="3" width="20" height="14" rx="1"/><text x="12" y="14.5" font-size="10" text-anchor="middle" fill="#999" stroke="none" font-family="Roboto,sans-serif" font-weight="700">$</text></svg>Payment</div>
    <div class="nav-item" style="top:604px">Invoices</div>
    <div class="nav-item" style="top:642px">Reports</div>
    <div class="nav-item" style="top:680px">Venues</div>
    <div class="nav-item" style="top:719px">Company</div>
    <div class="nav-item" style="top:757px">Settings</div>
    <div class="nav-item" style="top:796px">Help</div>
    <div class="nav-item" style="top:834px">Feedback</div>
  </nav>

  <div class="notice"><svg width="13" height="13" viewBox="0 0 24 24"><circle cx="12" cy="12" r="10" fill="none" stroke="var(--danger)" stroke-width="2.5"/><path d="M12 6v8M12 16.5v2" stroke="var(--danger)" stroke-width="2.5"/></svg>Notification: you can send your notification to the user</div>
  <div class="search">Search invoices<svg width="16" height="16" viewBox="0 0 24 24" fill="none" stroke="#666" stroke-width="2.6"><circle cx="10" cy="10" r="6"/><path d="M15 15l6 6"/></svg></div>
  <div class="fab" aria-label="New invoice"></div>

  <h2 class="title" style="top:188px">Overview</h2>

  <section class="card" style="left:119px;top:253px;width:683px;height:298px">
    <svg class="chart" width="683" height="298" viewBox="216 471 854 373" font-family="Roboto,sans-serif">
      <defs>
        <linearGradient id="gBlue" x1="0" y1="0" x2="0" y2="1"><stop offset="0" stop-color="#2d2a8c" stop-opacity=".22"/><stop offset="1" stop-color="#2d2a8c" stop-opacity="0"/></linearGradient>
        <linearGradient id="gOrange" x1="0" y1="0" x2="0" y2="1"><stop offset="0" stop-color="#f58a4b" stop-opacity=".25"/><stop offset="1" stop-color="#f58a4b" stop-opacity="0"/></linearGradient>
      </defs>
      <g stroke="#d6d6de" stroke-width="1">
        <line x1="275" y1="572" x2="1032" y2="572"/><line x1="275" y1="617" x2="1032" y2="617"/>
        <line x1="275" y1="661" x2="1032" y2="661"/><line x1="275" y1="706" x2="1032" y2="706"/>
        <line x1="275" y1="751" x2="1032" y2="751"/><line x1="275" y1="796" x2="1032" y2="796"/>
      </g>
      <g font-size="9.5" fill="#999">
        <text x="245" y="575">$2K</text><text x="245" y="620">$2K</text><text x="245" y="664">$500</text>
        <text x="245" y="709">$250</text><text x="245" y="754">$100</text><text x="245" y="799">$50</text>
      </g>
      <g font-size="9.5" fill="#999" text-anchor="middle">
        <text x="362" y="828">Mon</text><text x="468" y="828">Tue</text><text x="577" y="828">Wed</text>
        <text x="685" y="828">Thu</text><text x="790" y="828">Fri</text><text x="899" y="828">Sat</text><text x="1008" y="828">Sun</text>
      </g>
      <polygon points="360,751 467,661 574,707 685,573 791,662 899,618 1007,751 1007,790 360,790" fill="url(#gBlue)"/>
      <polygon points="359,706 467,638 578,686 684,636 791,727 900,573 1007,707 1007,790 359,790" fill="url(#gOrange)"/>
      <polyline points="360,751 467,661 574,707 685,573 791,662 899,618 1007,751" fill="none" stroke="var(--indigo)" stroke-width="1.2"/>
      <polyline points="359,706 467,638 578,686 684,636 791,727 900,573 1007,707" fill="none" stroke="var(--orange)" stroke-width="1.2"/>
      <g fill="var(--indigo)"><circle cx="360" cy="751" r="5"/><circle cx="467" cy="661" r="5"/><circle cx="574" cy="707" r="5"/><circle cx="685" cy="573" r="5"/><circle cx="791" cy="662" r="5"/><circle cx="899" cy="618" r="5"/><circle cx="1007" cy="751" r="5"/></g>
      <g fill="var(--orange)"><circle cx="359" cy="706" r="5"/><circle cx="467" cy="638" r="5"/><circle cx="578" cy="686" r="5"/><circle cx="684" cy="636" r="5"/><circle cx="791" cy="727" r="5"/><circle cx="900" cy="573" r="5"/><circle cx="1007" cy="707" r="5"/></g>
    </svg>
    <div class="pill on" style="left:18px;top:14px;width:67px">This Week</div>
    <div class="pill" style="left:97px;top:14px;width:67px">This Month</div>
    <div class="pill" style="left:176px;top:14px;width:67px">This Year</div>
    <div class="pill" style="left:255px;top:14px;width:67px">Last Year</div>
  </section>

  <section class="card totals" style="left:841px;top:253px;width:233px;height:298px">
    <h3>Total Invoices</h3>
    <div class="label" style="top:60px">Open Invoices</div>
    <div class="value" style="top:86px">$ 1500.00</div>
    <div class="label" style="top:133px">Paid Invoices</div>
    <div class="value" style="top:158px">$ 3500.00</div>
    <div class="label" style="top:206px">Unpaid Invoices</div>
    <div class="value" style="top:233px">$ 500.00</div>
  </section>

  <h2 class="title" style="top:605px">Overview</h2>

  <section class="card" style="left:119px;top:670px;width:963px;height:266px">
    <div class="pill on" style="left:18px;top:14px;width:67px">Open</div>
    <div class="pill" style="left:97px;top:14px;width:67px">Paid</div>
    <div class="pill" style="left:176px;top:14px;width:67px">unpaid</div>
    <div class="pill" style="left:255px;top:14px;width:67px">All</div>

    <div class="row" style="top:56px"><i class="check done"></i><span style="left:50px">Nathan Edwards</span><span style="left:281px">Bazaar Item #152100201</span><span style="left:569px">$250.00</span><span style="left:742px">09.09.2018</span>
      <svg style="left:856px" width="15" height="15" viewBox="0 0 24 24"><path d="M1 12s4-7 11-7 11 7 11 7-4 7-11 7S1 12 1 12z" fill="var(--indigo)"/><circle cx="12" cy="12" r="4" fill="#fff"/><circle cx="12" cy="12" r="2" fill="var(--indigo)"/></svg>
      <svg style="left:885px" width="15" height="15" viewBox="0 0 24 24" fill="none" stroke="#333" stroke-width="2.4"><path d="M20 14v7H3V5h7"/><path d="M9 15c1-5 5-8 11-8M15 3l5 4-5 4"/></svg>
      <svg style="left:914px" width="15" height="15" viewBox="0 0 24 24"><circle cx="12" cy="12" r="11" fill="var(--danger)"/><path d="M8 8l8 8M16 8l-8 8" stroke="#fff" stroke-width="2.6"/></svg></div>
    <div class="row" style="top:92px"><i class="check"></i><span style="left:50px">Phillip Herrera</span><span style="left:281px">Bazaar Item #252100201</span><span style="left:569px">$500.00</span><span style="left:742px">09.06.2018</span>
      <svg style="left:856px" width="15" height="15" viewBox="0 0 24 24"><path d="M1 12s4-7 11-7 11 7 11 7-4 7-11 7S1 12 1 12z" fill="var(--indigo)"/><circle cx="12" cy="12" r="4" fill="#fff"/><circle cx="12" cy="12" r="2" fill="var(--indigo)"/></svg>
      <svg style="left:885px" width="15" height="15" viewBox="0 0 24 24" fill="none" stroke="#333" stroke-width="2.4"><path d="M20 14v7H3V5h7"/><path d="M9 15c1-5 5-8 11-8M15 3l5 4-5 4"/></svg>
      <svg style="left:914px" width="15" height="15" viewBox="0 0 24 24"><circle cx="12" cy="12" r="11" fill="var(--danger)"/><path d="M8 8l8 8M16 8l-8 8" stroke="#fff" stroke-width="2.6"/></svg></div>
    <div class="row" style="top:128px"><i class="check"></i><span style="left:50px">Adam Williamson</span><span style="left:281px">Bazaar Item #168100201</span><span style="left:569px">$150.00</span><span style="left:742px">09.05.2018</span>
      <svg style="left:856px" width="15" height="15" viewBox="0 0 24 24"><path d="M1 12s4-7 11-7 11 7 11 7-4 7-11 7S1 12 1 12z" fill="var(--indigo)"/><circle cx="12" cy="12" r="4" fill="#fff"/><circle cx="12" cy="12" r="2" fill="var(--indigo)"/></svg>
      <svg style="left:885px" width="15" height="15" viewBox="0 0 24 24" fill="none" stroke="#333" stroke-width="2.4"><path d="M20 14v7H3V5h7"/><path d="M9 15c1-5 5-8 11-8M15 3l5 4-5 4"/></svg>
      <svg style="left:914px" width="15" height="15" viewBox="0 0 24 24"><circle cx="12" cy="12" r="11" fill="var(--danger)"/><path d="M8 8l8 8M16 8l-8 8" stroke="#fff" stroke-width="2.6"/></svg></div>
    <div class="row" style="top:164px"><i class="check"></i><span style="left:50px">Nicholas Hunt</span><span style="left:281px">Bazaar Item #152554201</span><span style="left:569px">$250.00</span><span style="left:742px">09.04.2018</span>
      <svg style="left:856px" width="15" height="15" viewBox="0 0 24 24"><path d="M1 12s4-7 11-7 11 7 11 7-4 7-11 7S1 12 1 12z" fill="var(--indigo)"/><circle cx="12" cy="12" r="4" fill="#fff"/><circle cx="12" cy="12" r="2" fill="var(--indigo)"/></svg>
      <svg style="left:885px" width="15" height="15" viewBox="0 0 24 24" fill="none" stroke="#333" stroke-width="2.4"><path d="M20 14v7H3V5h7"/><path d="M9 15c1-5 5-8 11-8M15 3l5 4-5 4"/></svg>
      <svg style="left:914px" width="15" height="15" viewBox="0 0 24 24"><circle cx="12" cy="12" r="11" fill="var(--danger)"/><path d="M8 8l8 8M16 8l-8 8" stroke="#fff" stroke-width="2.6"/></svg></div>
    <div class="row" style="top:200px"><i class="check"></i><span style="left:50px">Walter Reynolds</span><span style="left:281px">Bazaar Item #148430201</span><span style="left:569px">$110.00</span><span style="left:742px">09.03.2018</span>
      <svg style="left:856px" width="15" height="15" viewBox="0 0 24 24"><path d="M1 12s4-7 11-7 11 7 11 7-4 7-11 7S1 12 1 12z" fill="var(--indigo)"/><circle cx="12" cy="12" r="4" fill="#fff"/><circle cx="12" cy="12" r="2" fill="var(--indigo)"/></svg>
      <svg style="left:885px" width="15" height="15" viewBox="0 0 24 24" fill="none" stroke="#333" stroke-width="2.4"><path d="M20 14v7H3V5h7"/><path d="M9 15c1-5 5-8 11-8M15 3l5 4-5 4"/></svg>
      <svg style="left:914px" width="15" height="15" viewBox="0 0 24 24"><circle cx="12" cy="12" r="11" fill="var(--danger)"/><path d="M8 8l8 8M16 8l-8 8" stroke="#fff" stroke-width="2.6"/></svg></div>
    <div class="row" style="top:236px"><i class="check"></i><span style="left:50px">Peter Jenkins</span><span style="left:281px">Bazaar Item #254100201</span><span style="left:569px">$200.00</span><span style="left:742px">09.01.2018</span>
      <svg style="left:856px" width="15" height="15" viewBox="0 0 24 24"><path d="M1 12s4-7 11-7 11 7 11 7-4 7-11 7S1 12 1 12z" fill="var(--indigo)"/><circle cx="12" cy="12" r="4" fill="#fff"/><circle cx="12" cy="12" r="2" fill="var(--indigo)"/></svg>
      <svg style="left:885px" width="15" height="15" viewBox="0 0 24 24" fill="none" stroke="#333" stroke-width="2.4"><path d="M20 14v7H3V5h7"/><path d="M9 15c1-5 5-8 11-8M15 3l5 4-5 4"/></svg>
      <svg style="left:914px" width="15" height="15" viewBox="0 0 24 24"><circle cx="12" cy="12" r="11" fill="var(--danger)"/><path d="M8 8l8 8M16 8l-8 8" stroke="#fff" stroke-width="2.6"/></svg></div>

    <div class="scroll"><i></i></div>
  </section>
</div>
</body>
</html>
```